New Internet Service provider for regional or isolated businesses

I'm looking for a logo and basic information website for an Internet company - "Quill Ridge Networks". This new company will be providing specialised Internet connectivity for isolated areas or where connectivity is too expensive for one business.
i.e Linking Workplaces as one for faster, cheaper Web access.
3 Types of Pages
1. Home Page
2. Content Page templates
3. More Information Form
1. Contact Name. 2. Business Address. 3. Business Phone Number. 4. Mobile Phone. 5. Number of Staff 6. Current Internet connection . 7. Speed 8. Comments ?
Web Pages
**Quill Ridge Networks **
Linking Workplaces as one for faster Web access
Who is Quill Ridge Networks ?
How do we work ?
Which carriers ?
Technologies Used ?
Contact details
Check my address now ?
(Form)
Our company will be using Fibre and Microwave/Radio technology to connect remote businesses to high speed Internet
Target Market(s)
Business customers with minimum 10 staff outside metropolitan areas
Industry/Entity Type
Internet Service Provider
Coding
Coded - Design and coding required
Number of Pages Required
3 page
Requirements
Must have
- 3 Types of Pages
- 1. Home Page
- 2. Content Page templates (See above)
- 3. "More Information" Form
- 1. Contact Name. 2. Business Address. 3. Business Phone Number. 4. Mobile Phone. 5. Number of Staff 6.Current Internet connection . 7. Speed 8.Comments ?
Nice to have
- Pictures of fibre optics, radio towers, stock photos of businesses / PC's
- Some ideas on the companies we will be using (I am looking for something similar in my website).
- In order of preference
- 1. www.travenlo.com.au
- 2. www.pomrika.com,au
- 3.www.fendoly.com.au

```html
<!DOCTYPE html>
<html lang="en">
<head>
<meta charset="utf-8">
<title>Quill Ridge Networks</title>
<link href="https://fonts.googleapis.com/css2?family=Lato:ital,wght@0,300;0,400;0,700;0,900;1,400&display=swap" rel="stylesheet">
<style>
:root{
  --blue:#2f72b8;
  --blue-light:#2e8fd0;
  --dark:#2b2b2b;
  --ink:#1c1c1c;
  --text:#3a3a3a;
  --muted:#666;
  --line:#d6d6d6;
  --panel:#f0f0f0;
  --white:#fff;
}
*{box-sizing:border-box;margin:0;padding:0}
html,body{width:994px;height:1200px;overflow:hidden}
body{font-family:'Lato',sans-serif;color:var(--text);background:#fff;position:relative}
.abs{position:absolute}
.topstrip{left:0;top:0;width:994px;height:4px;background:var(--dark)}
.header{left:0;top:4px;width:994px;height:84px;background:#fafafa}
.zip-tab{left:548px;top:4px}
.zip-label{left:587px;top:8px;color:#fff;font-size:11px;font-weight:700;line-height:13px}
.zip-input{left:665px;top:10px;width:135px;height:20px;background:#fff;border:1px solid #bbb;font-size:10px;color:#999;padding:3px 4px}
.zip-go{left:807px;top:11px;width:44px;height:18px;background:var(--blue);color:#fff;border:1px solid #fff;font-size:11px;font-weight:700;text-align:center;line-height:16px}
.brand{left:108px;top:42px;font-size:29px;font-weight:300;color:var(--ink);letter-spacing:.3px}
.brand span{color:var(--blue-light)}
.contact-line{top:56px;font-size:14px;color:#333;display:flex;align-items:center;gap:6px}
.nav{left:0;top:88px;width:994px;height:34px;background:var(--blue)}
.nav a{position:absolute;top:0;height:34px;line-height:34px;color:#fff;font-size:11.5px;font-weight:700;text-decoration:none;letter-spacing:.5px}
.nav .active{background:var(--dark);padding:0 19px;left:109px}
.nav .sep{position:absolute;top:0;width:1px;height:34px;background:rgba(255,255,255,.18)}
.hero{left:0;top:122px;width:994px;height:388px;background:linear-gradient(160deg,#5d7fae 0%,#c6d6ea 30%,#e8eef6 50%,#8fb2dc 70%,#3a6ea8 100%)}
.hero-arrow{width:30px;height:30px;border-radius:50%;background:#eee;box-shadow:0 1px 3px rgba(0,0,0,.3)}
.tagline{left:0;top:430px;width:994px;text-align:center;font-size:27px;color:#fff;text-shadow:0 1px 3px rgba(0,0,0,.7)}
.backdrop{left:0;top:510px;width:994px;height:200px;background:linear-gradient(#e6e6e6,#fff)}
.features{left:108px;top:476px;width:776px;height:270px;background:#fff}
.feature{position:absolute;top:0;width:218px}
.feature h2,.section-title{font-size:19px;font-weight:700;color:var(--ink)}
.feature h2 span,.section-title span{color:var(--blue)}
.feature h2{position:absolute;top:12px;left:2px;white-space:nowrap}
.rule{position:absolute;height:1px;background:var(--line)}
.rule::before{content:"";position:absolute;left:0;top:-1px;width:78px;height:2px;background:var(--blue)}
.feature .rule{top:43px;left:0;width:218px}
.feature .pic{position:absolute;top:56px;left:0;width:218px;height:110px}
.feature p{position:absolute;top:174px;left:2px;width:218px;font-size:12px;line-height:17.5px;color:#333}
.readmore{position:absolute;top:236px;left:2px;height:16px;display:flex;font-size:10.5px;font-weight:700;color:#fff}
.readmore i{width:16px;background:var(--dark);font-style:normal;text-align:center;line-height:16px}
.readmore b{background:var(--blue);padding:0 5px;line-height:16px;margin-left:2px}
.vsep{top:496px;width:1px;height:220px;background:#eee}
.inquiry{left:108px;top:746px;width:777px;height:231px;background:var(--panel)}
.field{position:absolute;height:33px;background:#fff;border:1px solid #dcdcdc;border-radius:2px;font-size:12px;font-style:italic;color:#444;padding:0 10px;display:flex;align-items:center;justify-content:space-between}
.submit{position:absolute;height:30px;background:var(--blue);color:#fff;font-size:16px;font-weight:700;text-align:center;line-height:30px;border:1px solid #2560a0}
.carrier{position:absolute;top:1058px;height:63px;border:2px solid #ddd;background:#fff;display:flex;align-items:center;justify-content:center;gap:6px;font-size:18px;font-weight:700;color:#444}
.footer{left:0;top:1148px;width:994px;height:52px;background:#222}
.footer-links{left:108px;top:1166px;color:#fff;font-size:11.5px;font-weight:700;word-spacing:2px}
.copyright{right:110px;top:1166px;color:#ddd;font-size:10.5px}
</style>
</head>
<body>
<div class="abs topstrip"></div>
<div class="abs header"></div>
<svg class="abs zip-tab" width="340" height="34" viewBox="0 0 340 34"><path d="M0 0H338L318 26Q312 33 302 33H36Q26 33 20 26Z" fill="#2b2b2b"/></svg>
<div class="abs zip-label">Check Your<br>Address Now</div>
<div class="abs zip-input">Enter Zip Code</div>
<div class="abs zip-go">GO</div>

<div class="abs brand"><span>Quill Ridge</span> Networks</div>
<div class="abs contact-line" style="left:549px">
  <svg width="16" height="11" viewBox="0 0 16 11"><rect x=".5" y=".5" width="15" height="10" fill="#2f72b8"/><path d="M.5 .5L8 6L15.5 .5" stroke="#fff" fill="none"/></svg>
  info@quillridgenet.com</div>
<div class="abs contact-line" style="left:768px">
  <svg width="14" height="14" viewBox="0 0 14 14"><path d="M3 1L5 4L4 6Q6 9 8 10L10 9L13 11L11 13Q6 13 2 8Q0 4 3 1Z" fill="#2f72b8"/></svg>
  123-555-0147</div>

<nav class="abs nav">
  <a class="active" href="#">HOME</a>
  <a href="#" style="left:228px">WHO WE ARE</a>
  <span class="sep" style="left:350px"></span>
  <a href="#" style="left:397px">CARRIERS WE USE</a>
  <span class="sep" style="left:543px"></span>
  <a href="#" style="left:592px">TECHNOLOGIES USED</a>
  <span class="sep" style="left:760px"></span>
  <a href="#" style="left:808px">CONTACT</a>
</nav>

<div class="abs hero" role="img" aria-label="Rows of computer monitors overlaid with binary digits and a glowing world map"></div>
<svg class="abs hero-arrow" style="left:54px;top:296px" viewBox="0 0 30 30"><path d="M17 9L11 15L17 21" stroke="#333" stroke-width="3" fill="none"/></svg>
<svg class="abs hero-arrow" style="left:910px;top:296px" viewBox="0 0 30 30"><path d="M13 9L19 15L13 21" stroke="#333" stroke-width="3" fill="none"/></svg>
<div class="abs tagline">Linking Workplaces As One For Faster, Cheaper Web Access</div>

<div class="abs backdrop"></div>
<section class="abs features">
  <div class="feature" style="left:14px">
    <h2>About <span>Quill Ridge Networks</span></h2>
    <div class="rule"></div>
    <div class="pic" role="img" aria-label="Smiling businessman in an office with colleagues behind" style="background:linear-gradient(90deg,#dfe6ec,#b9c8d6 60%,#8ea6bf)"></div>
    <p>Lorem ipsum dolor sit amet, consectetuer adipiscing elit, sed diam nonummy nibh euismod magna aliquam erat volutpat.</p>
    <div class="readmore"><i>→</i><b>Read More</b></div>
  </div>
  <div class="feature" style="left:280px">
    <h2>Our Services <span>&amp; Plans</span></h2>
    <div class="rule"></div>
    <div class="pic" role="img" aria-label="Family of three generations gathered around a laptop" style="background:linear-gradient(90deg,#efe7df,#d9c4b0 50%,#ece4da)"></div>
    <p>Lorem ipsum dolor sit amet, consectetuer adipiscing elit, sed diam nonummy nibh euismod magna aliquam erat volutpat.</p>
    <div class="readmore"><i>→</i><b>Read More</b></div>
  </div>
  <div class="feature" style="left:547px">
    <h2>Technologies <span>Used</span></h2>
    <div class="rule"></div>
    <div class="pic" role="img" aria-label="Network cables and glowing fibre optic strands on blue" style="background:linear-gradient(135deg,#0d2a66,#2a5cb4 50%,#081a44)"></div>
    <p>Using Fibre and Microwave/Radio techno-logy to connect remote businesses to high speed Internet</p>
    <div class="readmore"><i>→</i><b>Read More</b></div>
  </div>
</section>
<div class="abs vsep" style="left:364px"></div>
<div class="abs vsep" style="left:630px"></div>

<section class="abs inquiry">
  <h2 class="section-title abs" style="left:15px;top:22px">Quick <span>Inquiry</span></h2>
  <div class="rule" style="left:14px;top:51px;width:758px"></div>
  <div class="field" style="left:14px;top:69px;width:180px">Contact Name</div>
  <div class="field" style="left:204px;top:69px;width:180px">Business Address</div>
  <div class="field" style="left:393px;top:69px;width:180px">Business Address</div>
  <div class="field" style="left:583px;top:69px;width:180px">Business Phone Number</div>
  <div class="field" style="left:14px;top:116px;width:180px">Mobile Phone</div>
  <div class="field" style="left:204px;top:116px;width:180px">Number of Staff
    <svg width="13" height="8" viewBox="0 0 13 8"><path d="M1 1L6.5 6.5L12 1" stroke="#555" stroke-width="1.4" fill="none"/></svg></div>
  <div class="field" style="left:393px;top:116px;width:370px">Current Internet Connection
    <span style="display:flex;align-items:center;gap:8px">Yes
      <svg width="14" height="14" viewBox="0 0 14 14"><rect x="1" y="3" width="10" height="10" fill="none" stroke="#2f72b8" stroke-width="1.5"/><path d="M3 7L6 10L13 1" stroke="#2f72b8" stroke-width="2" fill="none"/></svg>
      <span style="margin-left:24px">No</span>
      <svg width="14" height="14" viewBox="0 0 14 14"><rect x="1" y="2" width="11" height="11" fill="none" stroke="#555" stroke-width="1.5"/></svg></span></div>
  <div class="field" style="left:14px;top:170px;width:180px">Speed
    <svg width="13" height="8" viewBox="0 0 13 8"><path d="M1 1L6.5 6.5L12 1" stroke="#555" stroke-width="1.4" fill="none"/></svg></div>
  <div class="field" style="left:204px;top:170px;width:441px;align-items:flex-start;padding-top:8px">Message</div>
  <div class="submit" style="left:654px;top:172px;width:108px">Submit</div>
</section>

<h2 class="section-title abs" style="left:124px;top:1005px">Carriers <span>We Use</span></h2>
<svg class="abs" style="left:839px;top:1006px" width="34" height="24" viewBox="0 0 34 24"><path d="M12 2L3 12L12 22M22 2L31 12L22 22" stroke="#bbb" stroke-width="2" fill="none"/></svg>
<div class="rule abs" style="left:122px;top:1036px;width:750px"></div>

<div class="carrier" style="left:122px;width:121px">Veltra</div>
<div class="carrier" style="left:260px;width:136px">Norbright</div>
<div class="carrier" style="left:410px;width:163px"><span style="width:10px;height:10px;border-radius:50%;background:#2f72b8"></span>Kestrelink</div>
<div class="carrier" style="left:591px;width:117px">Ondaro</div>
<div class="carrier" style="left:720px;width:151px">Castwell</div>

<footer class="abs footer"></footer>
<div class="abs footer-links">Home &nbsp;| &nbsp;Who We Are &nbsp;| &nbsp;Carriers We Use &nbsp;| &nbsp;Technologies Used &nbsp;| &nbsp;Contact</div>
<div class="abs copyright">Copyright © 2016 Quill Ridge Networks. All Right Reserved.</div>
</body>
</html>
```